Business Card for Freelance Copywriting & Web Design Business

Hi! I have a logo but want a new business card. Here's a better idea of what I'm thinking:
-Brand new double-sided business card, rounded cards, embossed logo, nice quality paper
-Include phone (604-382-5194), email (hello@lauraberndt.org), and website (www.lauraberndt.org). No address, please, since I service clients worldwide.
-I'd like the fonts to match those on my website (www.lauraberndt.org). I had to purchase the one font (Born Ready), attached. I'm not sure which version was used on my site so I included all that I purchased. The secondary font is Helvetica
-I'd also like the tagline "Powerful Words. Impressive Results." included.
-My primary brand colour is the teal, colour #19ADC3
Laura Berndt | Laura Berndt Copywriting & Web Design <hello@lauraberndt.org>
-I'd also like the following services listed on the new cards:
SEO Website Content
SEO Blog Content
SEO Website Design
Contact Information for Business Card
as stated in brief
Font styles to use
Other font styles liked:
- See brief
Look and feel
Each slider illustrates characteristics of the customer's brand and the style your logo design should communicate.

```html
<!DOCTYPE html>
<html lang="en">
<head>
<meta charset="UTF-8">
<title>Laura Berndt Copywriting &amp; Web Design – Business Card</title>
<link rel="stylesheet" href="https://fonts.googleapis.com/css2?family=Lato:wght@400;700&display=swap">
<style>
  :root {
    --teal: #19adc3;
    --ink: #151515;
    --white: #ffffff;
    --paper-grey: #e4e4e6;
    --backdrop: #2a2a2e;
  }
  * { margin: 0; padding: 0; box-sizing: border-box; }
  html, body { width: 1200px; height: 947px; overflow: hidden; }
  body {
    background: var(--backdrop);
    font-family: "Lato", Helvetica, Arial, sans-serif;
    position: relative;
  }
  .card {
    position: absolute;
    left: 250px;
    width: 700px;
    height: 400px;
    border-radius: 26px;
    overflow: hidden;
  }
  .card--front { top: 50px; background: var(--teal); }
  .card--back { top: 497px; background: var(--white); }

  /* Front */
  .brand-name {
    position: absolute;
    color: var(--ink);
    font-weight: 700;
    text-align: center;
    line-height: 1.1;
  }
  .card--front .brand-name {
    left: 0; right: 0; top: 120px;
  }
  .brand-name__main { display: block; font-size: 56px; }
  .brand-name__sub { display: block; font-size: 18px; letter-spacing: 4px; text-transform: uppercase; margin-top: 10px; }
  .services {
    position: absolute;
    left: 0; right: 0; bottom: 62px;
    text-align: center;
    color: var(--white);
    font-size: 21px;
    letter-spacing: 0.3px;
  }

  /* Back */
  .card--back .brand-name {
    left: 36px; top: 150px; width: 270px;
  }
  .card--back .brand-name__main { font-size: 36px; }
  .card--back .brand-name__sub { font-size: 11px; letter-spacing: 2px; margin-top: 8px; }
  .divider {
    position: absolute;
    left: 330px; top: 95px;
    width: 1px; height: 170px;
    background: var(--teal);
  }
  .contact-block {
    position: absolute;
    left: 362px; top: 78px;
  }
  .contact-block__name {
    color: var(--teal);
    font-size: 36px;
    font-weight: 700;
    letter-spacing: 0.5px;
    line-height: 1;
  }
  .contact-block__role {
    color: var(--ink);
    font-size: 18px;
    margin-top: 6px;
  }
  .contact-list { list-style: none; margin-top: 22px; }
  .contact-list li {
    display: flex; align-items: center; gap: 12px;
    color: #333;
    font-size: 17px;
    line-height: 1.65;
  }
  .contact-list svg { width: 15px; height: 15px; flex: none; }
  .swoosh { position: absolute; inset: 0; }
  .tagline {
    position: absolute;
    left: 438px; top: 352px;
    color: var(--white);
    font-size: 17px;
    transform: rotate(-20deg);
    transform-origin: left top;
    white-space: nowrap;
  }
</style>
</head>
<body>
  <section class="card card--front" aria-label="Business card front">
    <div class="brand-name">
      <span class="brand-name__main">Laura Berndt</span>
      <span class="brand-name__sub">Copywriting &amp; Web Design</span>
    </div>
    <p class="services">SEO Website Content | SEO Blog Content | SEO Website Design</p>
  </section>

  <section class="card card--back" aria-label="Business card back">
    <svg class="swoosh" viewBox="0 0 700 400" preserveAspectRatio="none" aria-hidden="true">
      <path d="M250 400 Q 470 250 700 205 L700 222 Q 500 270 330 400 Z" fill="var(--paper-grey)"/>
      <path d="M340 400 Q 540 285 700 245 L700 400 Z" fill="var(--teal)"/>
    </svg>

    <div class="brand-name">
      <span class="brand-name__main">Laura Berndt</span>
      <span class="brand-name__sub">Copywriting &amp; Web Design</span>
    </div>

    <div class="divider"></div>

    <div class="contact-block">
      <h1 class="contact-block__name">LAURA BERNDT</h1>
      <p class="contact-block__role">Owner and Freelance Copywriter</p>
      <ul class="contact-list">
        <li>
          <svg viewBox="0 0 24 24" aria-hidden="true"><path fill="var(--teal)" d="M6.6 10.8a15 15 0 0 0 6.6 6.6l2.2-2.2c.3-.3.7-.4 1-.2 1.1.4 2.3.6 3.6.6.6 0 1 .4 1 1V20c0 .6-.4 1-1 1C10.6 21 3 13.4 3 4c0-.6.4-1 1-1h3.5c.6 0 1 .4 1 1 0 1.3.2 2.5.6 3.6.1.3 0 .7-.2 1z"/></svg>
          604-382-5194
        </li>
        <li>
          <svg viewBox="0 0 24 24" aria-hidden="true"><rect x="2" y="5" width="20" height="14" rx="1.5" fill="var(--teal)"/><path d="M3 6l9 7 9-7" stroke="#fff" stroke-width="1.8" fill="none"/></svg>
          hello@lauraberndt.org
        </li>
        <li>
          <svg viewBox="0 0 24 24" aria-hidden="true"><g fill="none" stroke="var(--teal)" stroke-width="1.8"><circle cx="12" cy="12" r="9.5"/><ellipse cx="12" cy="12" rx="4.5" ry="9.5"/><path d="M2.5 12h19M4 7h16M4 17h16"/></g></svg>
          www.lauraberndt.org
        </li>
      </ul>
    </div>

    <p class="tagline">Powerful Words. Impressive Results.</p>
  </section>
</body>
</html>
```